Speisekarten-Design für italienisches Restaurant im Golfclub mit Blick auf die Alpen
Zielgruppe
Italienisches Restaurant im Golfclub mit Blick auf die Alpen (bei gutem Wetter)
Aufgabenstellung
Karte muss weiterhin bearbeitet werden könne. Es geht um ein Design das optisch anspricht aber nicht übertrieben ist. Die Blätter kommen später in eine Menukarte die noch in Auftrag gegeben werden.
Im Idealfall kann der Designer hierfür auch was mit designen das an einen Firma weitergeben werden kann um die 'Umschläge zu erstellen. Logo kann muss nicht mit drin sein. Es geht auch sehr um die einfache Darstellung des Ganzen.

```html
<!DOCTYPE html>
<html lang="de">
<head>
<meta charset="utf-8">
<title>Speisekarte – Tagesmenüs, Vorspeisen, Pasta</title>
<link rel="stylesheet" href="https://fonts.googleapis.com/css2?family=Fira+Sans+Condensed:wght@300;400&family=Fira+Sans:wght@600&display=swap">
<style>
  :root {
    --paper: #ffffff;
    --ink: #2a2a2a;
    --ink-soft: #3a3a3a;
    --rule: #c9c9c9;
    --grass: #8fd38b;
    --grass-light: #e3f4e1;
    --base-line: #cfcfcf;
  }
  * { margin: 0; padding: 0; box-sizing: border-box; }
  html, body { width: 1200px; height: 812px; overflow: hidden; background: var(--paper); }
  .menu-card {
    position: relative; width: 1200px; height: 812px;
    font-family: "Fira Sans Condensed", "Arial Narrow", sans-serif;
    font-weight: 300; color: var(--ink);
  }
  .section-title {
    position: absolute; font-family: "Fira Sans", Arial, sans-serif;
    font-weight: 600; font-size: 17px; letter-spacing: 0.5px; color: var(--ink);
    transform: translateX(-50%);
  }
  .daily-title { left: 290px; top: 50px; }
  .starters-title { left: 908px; top: 50px; }
  .pasta-title { left: 908px; top: 362px; }

  .set-menu { position: absolute; left: 65px; font-size: 17px; line-height: 20.8px; color: var(--ink-soft); }
  .set-menu h3 { font-family: "Fira Sans Condensed", sans-serif; font-weight: 400; font-size: 17px; color: var(--ink); }
  .set-menu .price { font-size: 15px; }
  .menu-one { top: 120px; }
  .menu-two { top: 314px; }
  .menu-three { top: 494px; }

  .dish-list { position: absolute; left: 667px; width: 500px; list-style: none; }
  .dish-list li {
    display: flex; justify-content: space-between;
    border-bottom: 1px solid var(--rule);
    font-size: 15.5px; line-height: 19.8px; padding-right: 6px;
  }
  .dish-list .dish-price { text-align: right; }
  .starters { top: 120px; }
  .pasta { top: 430px; }

  .landscape-area {
    position: absolute; left: 0; top: 688px; width: 1200px; height: 92px;
    background: linear-gradient(to bottom, var(--paper) 0%, var(--grass-light) 55%, var(--grass) 100%);
  }
  .base-line {
    position: absolute; left: 0; top: 801px; width: 1200px; height: 2px;
    background: var(--base-line);
  }
</style>
</head>
<body>
<main class="menu-card">
  <h2 class="section-title daily-title">TAGESMENÜS</h2>

  <section class="set-menu menu-one">
    <h3>MENU 1</h3>
    <p>Appetithäppchen und Aperitif</p>
    <p>Italiensicher Aufschnitt Teller</p>
    <p>Pasta mit Hackfleischsoße und Sahne</p>
    <p>Kalbsbraten mit Barolosoße und Rosmarin Kartoffeln</p>
    <p>Zitronen Sorbet</p>
    <p class="price">49,-</p>
  </section>

  <section class="set-menu menu-two">
    <h3>MENU 2</h3>
    <p>Gemischter Salat</p>
    <p>Pasta mit scharfer Tomatensoße</p>
    <p>Putengeschnetzeltes in Currysoße mit Reis</p>
    <p>Tiramisu</p>
    <p class="price">35,-</p>
  </section>

  <section class="set-menu menu-three">
    <h3>MENU 3</h3>
    <p>Aperitif</p>
    <p>Vitello Tonnato</p>
    <p>Lasagne im Ofen überbacken</p>
    <p>Rumpsteak tranchiert, auf Rucola Bett</p>
    <p>serviert mit gehobelten Original Parmesan Käse</p>
    <p>Rosmarinkartoffeln und Gemüse</p>
    <p>Panna Cotta mit Waldfrüchte</p>
    <p class="price">55,-</p>
  </section>

  <h2 class="section-title starters-title">VORSPEISEN</h2>
  <ul class="dish-list starters">
    <li><span>Vorspeise Teller nach Art des Hauses</span><span class="dish-price">12,-</span></li>
    <li><span>Meeresfrüchte Vorspeise</span><span class="dish-price">14,-</span></li>
    <li><span>Aufschnitt und Meeresfrüchte Vorspeise</span><span class="dish-price">14,-</span></li>
    <li><span>Rinder Carpaccio</span><span class="dish-price">12,-</span></li>
    <li><span>Gemischter Salat</span><span class="dish-price">5,-</span></li>
    <li><span>Vitello Tonnato</span><span class="dish-price">12,-</span></li>
    <li><span>Bruschetta 2 Stück</span><span class="dish-price">4,-</span></li>
    <li><span>Gemüse Vorspeise</span><span class="dish-price">10,-</span></li>
    <li><span>Crevetten Cochtail</span><span class="dish-price">11,-</span></li>
  </ul>

  <h2 class="section-title pasta-title">PASTA</h2>
  <ul class="dish-list pasta">
    <li><span>Lasagne im Ofen überbacken</span><span class="dish-price">12,-</span></li>
    <li><span>Paccheri mit Hackfleischsoße</span><span class="dish-price">12,-</span></li>
    <li><span>Ravioli mit Ricotta- und Spinatfüllung</span><span class="dish-price">13,-</span></li>
    <li><span>Risotto mit Steinpilzsoße</span><span class="dish-price">13,-</span></li>
    <li><span>Gnocchi mit Tomatensoße und Mozzarella</span><span class="dish-price">12,-</span></li>
    <li><span>Tortellini mit Rahmsoße</span><span class="dish-price">12,-</span></li>
    <li><span>Zweierlei Pasta</span><span class="dish-price">13,-</span></li>
    <li><span>Orecchiette mit Gemüse</span><span class="dish-price">12,-</span></li>
  </ul>

  <div class="landscape-area" role="img" aria-label="Grüne Hügellinie eines Golfplatzes mit Fahne"></div>
  <div class="base-line"></div>
</main>
</body>
</html>
```